3D printers services needs a brochure

We need a Creative, Innovative idea for a brochure. 3d printing for Prototyping, .
We would like to have an A4 horizontal brochure that could give a 3D effect when folded or cut.
Our name is K7! Spark! Build! Soar! our website is www.k7momentum.com. Please be inspired by our logo and the dreamy cloud part.
Our prospects: Architects, Artists, Museums and Designers ( Jewellery, watches, etc ...)
What we offer:
.3D printing and prototyping.
.3D scanning.
.Transforming 2D images to 3D objects.
. Making their Portals where clients can visualize, personalize (IN 3D) and order their work.

Reason: I would like to extend it because i figured out the deadline is too short! Thank you Best regards Fadri

Printing

```html
<!DOCTYPE html>
<html lang="en">
<head>
<meta charset="utf-8">
<title>K7 – 3D Printing Brochure</title>
<link href="https://fonts.googleapis.com/css2?family=Roboto+Condensed:wght@400;700&family=Roboto+Slab:wght@300;400&family=Quicksand:wght@500;700&display=swap" rel="stylesheet">
<style>
  :root{
    --green:#78d10d;
    --green-dark:#5aa80a;
    --grey:#5b5b5b;
    --grey-light:#9a9a9a;
    --ink:#2b2b2b;
    --paper:#ffffff;
    --backdrop:#ecebe8;
    --fold:#d6d6d6;
  }
  *{box-sizing:border-box;margin:0;padding:0}
  html,body{width:1200px;height:861px;overflow:hidden;background:var(--backdrop)}
  .brochure{position:absolute;left:74px;top:20px;width:1052px;height:821px;background:var(--paper);overflow:hidden;box-shadow:0 2px 10px rgba(0,0,0,.18)}
  .shapes{position:absolute;inset:0}
  .abs{position:absolute}
  .headline{font-family:"Roboto Condensed",sans-serif;font-weight:700;color:var(--green)}
  .body-text{font-family:"Roboto Slab",serif;font-weight:300;color:var(--ink);font-size:14px;line-height:19px}
  .tagline{font-family:"Quicksand",sans-serif;font-weight:500;color:var(--grey);letter-spacing:.5px;white-space:nowrap}
  .brand{font-family:"Quicksand",sans-serif;font-weight:700;color:var(--grey);display:flex;align-items:center}
  .brand .mark{background:var(--green);display:inline-block}

  /* Panel 1 */
  .prospects{left:0;width:355px;top:446px;text-align:center;font-family:"Roboto Condensed",sans-serif;font-size:17px;line-height:22px;color:var(--grey)}
  .offer-title{left:27px;top:498px;font-size:23px;line-height:28px}
  .offer-rule{left:27px;top:527px;width:280px;height:1px;background:#cfcfcf}
  .offer-list{left:38px;top:537px;width:255px;list-style:none}
  .offer-list li{position:relative;padding-left:17px;margin-bottom:12px;font-size:13.5px;line-height:17px;font-family:"Roboto Slab",serif;font-weight:300;color:var(--ink)}
  .offer-list li::before{content:"";position:absolute;left:0;top:4px;width:8px;height:8px;background:var(--green);border-radius:2px}
  .phone-line{font-family:"Roboto Condensed",sans-serif;font-weight:700;color:var(--ink);display:flex;align-items:center;gap:4px;white-space:nowrap}
  .p1-phone{left:26px;top:777px;font-size:19px}

  /* Panel 2 */
  .bubble{left:378px;top:44px;width:294px;height:112px;border-radius:56px;background:var(--paper);box-shadow:0 3px 8px rgba(0,0,0,.25);display:flex;align-items:center;justify-content:center;text-align:center;font-size:21px;line-height:27px}
  .intro{left:378px;top:200px;width:245px}
  .intro p{margin-bottom:7px}
  .partner{border-radius:10px}
  .partner-a{left:378px;top:328px;width:125px;height:72px;background:linear-gradient(#e4f1fb,#bcdcf2)}
  .partner-b{left:560px;top:325px;width:70px;height:70px;background:#2f7fb0;transform:rotate(45deg) scale(.7);border-radius:6px}
  .p2-brand{left:390px;top:478px;font-size:44px;line-height:50px;gap:10px}
  .p2-brand .mark{width:14px;height:14px}
  .p2-tagline{left:384px;top:558px;font-size:12.5px}
  .contact{left:376px;width:300px;display:flex;align-items:flex-start;gap:8px;font-family:"Roboto Slab",serif;font-weight:300;font-size:13px;line-height:18px;color:var(--ink)}
  .contact svg{flex:none;margin-top:3px}
  .social{left:580px;top:777px;display:flex;gap:9px}
  .social span{width:27px;height:27px;border-radius:50%;background:#2a6fb6;border:2px solid var(--ink)}

  /* Panel 3 */
  .p3-brand{left:790px;top:158px;font-size:90px;line-height:100px;gap:16px}
  .p3-brand .mark{width:22px;height:22px}
  .p3-tagline{left:697px;width:355px;top:294px;text-align:center;font-size:22px}
  .p3-phone{left:697px;width:355px;top:742px;justify-content:center;font-size:23px}
  .p3-web{left:697px;width:355px;top:781px;font-family:"Roboto Slab",serif;font-weight:300;font-size:14px;color:var(--ink);display:flex;justify-content:center;align-items:center;gap:5px}
</style>
</head>
<body>
<main class="brochure">
  <svg class="shapes" viewBox="0 0 1052 821" width="1052" height="821">
    <defs>
      <linearGradient id="workshop" x1="0" y1="0" x2="1" y2="1">
        <stop offset="0" stop-color="#6a7a8c"/><stop offset=".5" stop-color="#4a4c52"/><stop offset="1" stop-color="#2e2f33"/>
      </linearGradient>
      <linearGradient id="plan" x1="0" y1="0" x2="1" y2="1">
        <stop offset="0" stop-color="#e8e8e8"/><stop offset=".55" stop-color="#9fd64a"/><stop offset="1" stop-color="#d9d9d9"/>
      </linearGradient>
    </defs>
    <!-- top band -->
    <rect x="0" y="0" width="1052" height="100" fill="var(--green)"/>
    <path d="M0 96 Q180 58 355 112 Q420 132 460 112 L460 60 L640 60 L640 112 Q700 100 760 88 Q900 60 1052 72 V821 H0 Z" fill="var(--paper)"/>
    <path d="M0 86 Q180 50 360 104" stroke="var(--grey)" stroke-width="7" fill="none"/>
    <path d="M700 92 Q880 60 1052 64" stroke="var(--grey)" stroke-width="9" fill="none"/>
    <!-- workshop photo -->
    <g role="img" aria-label="Photo of a technician in a hard hat 3D scanning a metal part next to a laptop">
      <path d="M0 98 Q180 64 355 118 V420 Q200 400 0 436 Z" fill="url(#workshop)"/>
    </g>
    <path d="M0 440 Q180 402 355 428 V440 Q180 420 0 455 Z" fill="var(--paper)"/>
    <path d="M30 452 Q200 412 340 424" stroke="var(--grey-light)" stroke-width="4" fill="none"/>
    <!-- architectural render -->
    <path d="M697 376 Q880 348 1052 362" stroke="var(--grey)" stroke-width="9" fill="none"/>
    <g role="img" aria-label="Architectural 3D floor plan render with green highlighted rooms">
      <path d="M697 382 Q880 356 1052 370 V712 Q880 704 697 722 Z" fill="url(#plan)"/>
    </g>
    <!-- bottom band -->
    <path d="M0 728 Q200 712 355 770 Q450 802 540 782 Q620 764 697 746 Q860 722 1052 732 V821 H0 Z" fill="var(--green)"/>
    <path d="M0 716 Q200 700 355 758 Q450 790 540 770 Q620 752 697 734" stroke="var(--grey)" stroke-width="8" fill="none"/>
    <!-- folds -->
    <line x1="355" y1="0" x2="355" y2="821" stroke="var(--fold)" stroke-width="1"/>
    <line x1="697" y1="0" x2="697" y2="821" stroke="var(--fold)" stroke-width="1"/>
  </svg>

  <!-- Panel 1 -->
  <p class="abs prospects">Our prospects: Architects,<br>Artists, Museums and Designers</p>
  <h2 class="abs headline offer-title">What we offer:</h2>
  <div class="abs offer-rule"></div>
  <ul class="abs offer-list">
    <li>3D printing and prototyping</li>
    <li>3D scanning</li>
    <li>Transforming 2D images to 3D objects</li>
    <li>Making their Portals where clients can visualize, personalize (IN 3D) and order their work</li>
  </ul>
  <div class="abs phone-line p1-phone">
    <svg width="18" height="18" viewBox="0 0 24 24"><circle cx="12" cy="12" r="10.5" fill="none" stroke="currentColor" stroke-width="2"/><path d="M8 6.5l2 .2 1 3-1.3 1.1a7 7 0 0 0 3.5 3.5l1.1-1.3 3 1 .2 2c-.4.9-1.5 1.4-2.6 1.2A10 10 0 0 1 6.8 9.1C6.6 8 7.1 6.9 8 6.5z" fill="currentColor"/></svg>
    4179 555 0142
  </div>

  <!-- Panel 2 -->
  <div class="abs headline bubble">We are experts in<br>3D designing, scanning and<br>printing technologies.</div>
  <div class="abs body-text intro">
    <p>We are independant to offer you the best in class products.</p>
    <p>We base our experience on a 15 years Software solutions company and the first Swiss 3D manufacturer.</p>
  </div>
  <div class="abs partner partner-a"></div>
  <div class="abs partner-b"></div>
  <div class="abs brand p2-brand"><span class="mark"></span>K7</div>
  <p class="abs tagline p2-tagline">SPARK! BUILD! SOAR!</p>
  <div class="abs contact" style="top:589px">
    <svg width="11" height="14" viewBox="0 0 12 16"><path d="M6 0a6 6 0 0 1 6 6c0 4-6 10-6 10S0 10 0 6a6 6 0 0 1 6-6zm0 3.5a2.5 2.5 0 1 0 0 5 2.5 2.5 0 0 0 0-5z" fill="var(--green)"/></svg>
    <span>Rue des Alpes 48, Geneva 1201<br>Switzerland</span>
  </div>
  <div class="abs contact" style="top:644px">
    <svg width="14" height="11" viewBox="0 0 14 11"><rect x=".75" y=".75" width="12.5" height="9.5" fill="none" stroke="var(--green)" stroke-width="1.5"/><path d="M1 1l6 5 6-5" fill="none" stroke="var(--green)" stroke-width="1.5"/></svg>
    <span>Fadri@K7momentum.org</span>
  </div>
  <div class="abs contact" style="top:665px">
    <svg width="13" height="13" viewBox="0 0 14 14"><circle cx="7" cy="7" r="6" fill="none" stroke="var(--green)" stroke-width="1.4"/><ellipse cx="7" cy="7" rx="2.6" ry="6" fill="none" stroke="var(--green)" stroke-width="1.2"/><path d="M1 7h12" stroke="var(--green)" stroke-width="1.2"/></svg>
    <span>www.k7momentum.com</span>
  </div>
  <div class="abs contact" style="top:699px">
    <svg width="13" height="13" viewBox="0 0 24 24"><circle cx="12" cy="12" r="10.5" fill="none" stroke="var(--green)" stroke-width="2"/><path d="M8 6.5l2 .2 1 3-1.3 1.1a7 7 0 0 0 3.5 3.5l1.1-1.3 3 1 .2 2c-.4.9-1.5 1.4-2.6 1.2A10 10 0 0 1 6.8 9.1C6.6 8 7.1 6.9 8 6.5z" fill="var(--green)"/></svg>
    <span>4179 555 0142</span>
  </div>
  <div class="abs contact" style="top:718px">
    <svg width="13" height="13" viewBox="0 0 14 14"><rect x="3" y="1" width="8" height="4" fill="none" stroke="var(--green)" stroke-width="1.3"/><rect x="1" y="5" width="12" height="5" fill="none" stroke="var(--green)" stroke-width="1.3"/><rect x="3" y="9" width="8" height="4" fill="var(--paper)" stroke="var(--green)" stroke-width="1.3"/></svg>
    <span>4179 555 0142</span>
  </div>
  <div class="abs social" aria-label="Social media links"><span></span><span></span><span></span></div>

  <!-- Panel 3 -->
  <div class="abs brand p3-brand"><span class="mark"></span>K7</div>
  <p class="abs tagline p3-tagline">SPARK! BUILD! SOAR!</p>
  <div class="abs phone-line p3-phone">
    <svg width="21" height="21" viewBox="0 0 24 24"><circle cx="12" cy="12" r="10.5" fill="none" stroke="currentColor" stroke-width="2"/><path d="M8 6.5l2 .2 1 3-1.3 1.1a7 7 0 0 0 3.5 3.5l1.1-1.3 3 1 .2 2c-.4.9-1.5 1.4-2.6 1.2A10 10 0 0 1 6.8 9.1C6.6 8 7.1 6.9 8 6.5z" fill="currentColor"/></svg>
    4179 555 0142
  </div>
  <div class="abs p3-web">
    <svg width="13" height="13" viewBox="0 0 14 14"><circle cx="7" cy="7" r="6" fill="none" stroke="var(--ink)" stroke-width="1.4"/><ellipse cx="7" cy="7" rx="2.6" ry="6" fill="none" stroke="var(--ink)" stroke-width="1.2"/><path d="M1 7h12" stroke="var(--ink)" stroke-width="1.2"/></svg>
    www.k7momentum.com
  </div>
</main>
</body>
</html>
```